Banner for homepage

It is a new banner for the homepage, temporary site address is 61.187.40.72 ( is the biggest banner only ) . Would be 5 variations for image content as below (in Portuguese ) :

Image 1:
Leitor de codigo de barras
Todos os tipos de leitores de código de barras para as mais diversas aplicações.
( example of product images in : http://www.quentorlabs.com/en-US/Pages/Category.aspx?category=barcode-scanners&cat=KLT)

Image 2:
Impressora de etiquetas
Identifique o que for nessário com o melhor custo/beneficio e flexibilidade de materiais de impressão.
( example of product images in : vintor.com in label printers desktop and industrial)

Image 3:
Impressora de cupom
Imprima recibos e cupons fiscais com agilidade e qualidade, temos a impressora certa para o seu PDV.
( example of product images in : http://www.palutrek.com.br/equipamento-categoria-impressoras+fiscais.html)

Image 4:
Coletor de dados
Computadores móveis com leitor de código de barras, que levam a automação para frente de trabalho.
( example of product images in : http://www.quentorlabs.com/en-US/Pages/Category.aspx?cat=KLT&category=hand-held-mobile-computer)

Image 5:
Etiquetas e Ribbons:
Etiquetas adesivas e não adesivas em vários de tipos de materiais, papéis e plásticos. O ribbon certo para impressão perfeita em cada material.
( example of product images in : http://www.tagmirelo.com/cats/supplies/barcode-printer.htm?nav=hdr)

```html
<!DOCTYPE html>
<html lang="pt-BR">
<head>
<meta charset="utf-8">
<title>Korvex — Soluções em Automação e Código de barras</title>
<link rel="stylesheet" href="https://fonts.googleapis.com/css2?family=Oswald:wght@300;400;500&family=Yanone+Kaffeesatz:wght@300;400&family=Cabin+Condensed:wght@400;500&family=Arimo:wght@400;700&display=swap">
<style>
:root{
  --red:#c8323a;
  --page:#ececec;
  --nav-edge:#2a2a2a;
  --ink:#3a3a3a;
  --white:#ffffff;
  --gold:#d7b27a;
  --card:#f7f7f7;
}
*{box-sizing:border-box;margin:0;padding:0}
html,body{width:1200px;height:923px;overflow:hidden}
body{background:var(--page);font-family:"Arimo",Arial,sans-serif;color:var(--ink);position:relative}
.header{position:absolute;left:0;top:0;width:1200px;height:92px;background:var(--red)}
.brand{position:absolute;left:172px;top:9px;width:251px;height:40px;background:var(--white);border-radius:20px;display:flex;align-items:center;justify-content:center;gap:10px}
.brand-dot{width:14px;height:14px;background:var(--red);border-radius:50%}
.brand-name{font-family:"Oswald",sans-serif;font-weight:500;font-size:24px;letter-spacing:5px;color:#1c1c1c}
.tagline{position:absolute;left:185px;top:53px;font-size:11.5px;color:#fbe3e3}
.toplinks{position:absolute;right:169px;top:10px;display:flex;font-size:10.5px;font-weight:700;color:var(--white)}
.toplinks span{padding:0 9px;border-left:1px solid #f1b3b6}
.toplinks span:first-child{border-left:0}
.toplinks span:last-child{padding-right:0}
.hbox{position:absolute;top:32px;height:41px;background:var(--white);padding:5px 10px;font-family:"Oswald",sans-serif;line-height:1}
.hbox b{display:block;font-weight:400;font-size:15px;color:#3b3b3b}
.hbox small{display:block;font-size:10px;color:#e0442b;margin-top:4px}
.chat{left:798px;width:96px}
.phones{left:909px;width:124px}
.phones svg{position:absolute;right:10px;top:18px}
.nav{position:absolute;left:148px;top:83px;width:904px;height:36px;background:linear-gradient(#474747,#333);border:1px solid var(--nav-edge);border-radius:3px;display:flex;align-items:center}
.nav a{flex:none;font-family:"Oswald",sans-serif;font-weight:300;font-size:11px;letter-spacing:-.3px;color:#f2f2f2;text-align:center;white-space:nowrap;height:34px;line-height:34px;border-right:1px solid #262626;box-shadow:1px 0 0 #555;text-decoration:none}
.search{position:absolute;right:8px;top:6px;width:131px;height:22px;background:#2c2c2c;border:1px solid #222;border-radius:2px;font-size:10px;color:#aaa;padding:4px 6px}
.search svg{position:absolute;right:5px;top:4px}
.hero{position:absolute;left:166px;top:138px;width:646px;height:296px;border-radius:8px;overflow:hidden;background:#f3f3f3;box-shadow:0 1px 3px rgba(0,0,0,.2)}
.hero-photo{position:absolute;left:400px;top:0;width:246px;height:296px;background:radial-gradient(ellipse at 50% 50%,#6a6b6e,#3a3b3d 60%,#2b2b2c)}
.hero-title{position:absolute;left:19px;top:103px;font-family:"Cabin Condensed",sans-serif;font-weight:400;font-size:34px;letter-spacing:-1px;color:#3c3c3c}
.hero-title em{font-style:normal;color:var(--red)}
.hero-band{position:absolute;left:0;top:145px;width:400px;height:51px;background:#d3d3d3}
.hero-band p{position:absolute;left:22px;top:7px;font-size:13px;line-height:19px;color:#262626;width:372px}
.hero-cta{position:absolute;left:16px;top:211px;width:127px;height:33px;background:var(--red);border-radius:2px;color:var(--white);font-family:"Oswald",sans-serif;font-weight:300;font-size:20px;display:flex;align-items:center;justify-content:center;gap:6px}
.promo{position:absolute;left:833px;width:204px;height:140px;border:1px solid #d0d0d0;overflow:hidden}
.promo.fast{top:139px;background:linear-gradient(135deg,#2c2c2c,#1d1d1d)}
.promo.invoice{top:293px;background:linear-gradient(135deg,#8f847c,#6e655f)}
.promo h3{position:absolute;left:22px;top:14px;font-family:"Oswald",sans-serif;font-weight:500;font-size:26px;letter-spacing:-.5px;color:var(--gold);line-height:1}
.promo h3 span{color:var(--white)}
.promo.invoice h3{color:#3d3936;left:21px}
.promo p{position:absolute;left:22px;top:56px;font-size:11px;line-height:17px;color:var(--white);width:110px}
.promo .btn{position:absolute;left:20px;top:99px;width:82px;height:20px;border-radius:10px;font-family:"Oswald",sans-serif;font-size:11px;color:var(--white);text-align:center;line-height:20px}
.fast .btn{background:linear-gradient(#d9b07c,#a77a48)}
.invoice .btn{background:linear-gradient(#e1443c,#b3211b)}
.promo .pic{position:absolute;right:0;bottom:0;width:82px;height:72px}
.fast .pic{background:linear-gradient(160deg,#e5913e,#9b4d12)}
.invoice .pic{background:linear-gradient(160deg,#1c5b63,#0b1e22)}
.section-title{position:absolute;left:175px;font-family:"Oswald",sans-serif;font-weight:400;font-size:17px;color:#3a3a3a}
.stripe{position:absolute;left:166px;width:886px;height:14px;background:repeating-linear-gradient(45deg,#dcdcdc 0 2px,#efefef 2px 4px)}
.card{position:absolute;top:595px;width:203px;height:340px;background:var(--card);box-shadow:0 0 2px rgba(0,0,0,.12)}
.card .thumb{position:absolute;left:13px;top:14px;width:177px;height:176px;border:1px solid #e0e0e0;background:radial-gradient(ellipse at 50% 52%,#d9d9d9 0,#eeeeee 35%,#ffffff 60%)}
.card h4{position:absolute;left:14px;top:194px;width:180px;font-family:"Yanone Kaffeesatz",sans-serif;font-weight:300;font-size:18px;line-height:28px;color:#555}
.card h4::first-letter{color:var(--red)}
</style>
</head>
<body>
<header class="header">
  <div class="brand"><span class="brand-dot"></span><span class="brand-name">KORVEX</span></div>
  <div class="tagline">Soluções em Automação e Código de barras</div>
  <div class="toplinks"><span>Principal</span><span>Quem Somos</span><span>Entre em Contato</span></div>
  <div class="hbox chat"><b>CHAT ONLINE</b><small>CLIQUE AQUI</small></div>
  <div class="hbox phones"><b>TELEFONES</b><small>TODOS OS ESTADOS</small>
    <svg width="9" height="6" viewBox="0 0 9 6"><path d="M0 0h9L4.5 6z" fill="#444"/></svg></div>
</header>
<nav class="nav">
  <a style="width:146px">LEITOR DE CÓDIGO DE BARRAS</a><a style="width:131px">IMPRESSORA DE ETIQUETAS</a><a style="width:120px">AUTOMAÇÃO COMERCIAL</a><a style="width:65px">ETIQUETAS</a><a style="width:97px">COLETOR DE DADOS</a><a style="width:120px">IMPRESSORA DE CARTÃO</a><a style="width:56px">MARCAS</a>
  <div class="search">Busca<svg width="11" height="11" viewBox="0 0 11 11"><circle cx="4.5" cy="4.5" r="3.3" fill="none" stroke="#ddd" stroke-width="1.5"/><path d="M7 7l3 3" stroke="#ddd" stroke-width="2"/></svg></div>
</nav>
<section class="hero">
  <div class="hero-photo" role="img" aria-label="Impressora de etiquetas desktop imprimindo uma etiqueta"></div>
  <h2 class="hero-title"><em>Impressora</em> De Etiquetas</h2>
  <div class="hero-band"><p>Identifique o que for nessário com o melhor custo/beneficio e flexibilidade de materiais de impressão.</p></div>
  <div class="hero-cta">LEARN MORE <svg width="12" height="14" viewBox="0 0 12 14"><path d="M0 0l6 7-6 7zM6 0l6 7-6 7z" fill="#fff"/></svg></div>
</section>
<aside class="promo fast">
  <h3>Entrega<span>Rápida</span></h3>
  <p>Enviamos sua compra para todo o Brasil.</p>
  <div class="btn">Leia Mais</div>
  <div class="pic" role="img" aria-label="Caixa de papelão de entrega"></div>
</aside>
<aside class="promo invoice">
  <h3>Boleto<span>Faturado</span></h3>
  <p>Receba seu pedido com os boletos.</p>
  <div class="btn">Leia Mais</div>
  <div class="pic" role="img" aria-label="Sacola de compras"></div>
</aside>
<h2 class="section-title" style="top:460px">DESTAQUES</h2>
<div class="stripe" style="top:492px"></div>
<h2 class="section-title" style="top:532px">NOVIDADES</h2>
<div class="stripe" style="top:564px"></div>
<article class="card" style="left:175px"><div class="thumb" role="img" aria-label="Rolos de etiquetas adesivas"></div><h4>Etiqueta Papel Couche Adesiva 43mm X 94mm X 02 Colunas Separadas</h4></article>
<article class="card" style="left:397px"><div class="thumb" role="img" aria-label="Rolos de etiquetas adesivas"></div><h4>Etiqueta Papel Couche Adesiva 40mm X 70mm X 02 Colunas Separadas</h4></article>
<article class="card" style="left:618px"><div class="thumb" role="img" aria-label="Rolos de etiquetas adesivas"></div><h4>Etiqueta Papel Couche Adesiva 30mm X 35mm X 03 Colunas Separadas</h4></article>
<article class="card" style="left:840px"><div class="thumb" role="img" aria-label="Rolos de etiquetas adesivas"></div><h4>Etiqueta Papel Couche Adesiva 60mm X 60mm X 01 Coluna</h4></article>
</body>
</html>
```